Werbe-Email-Design
Zielgruppe
Wir sind Dienstleister in der Industrie/ Automobilindustrie. Die Zielgruppe für unsere Werbe-Email sind potenzielle Kunden (möglichst Einkäufer) für unser Produkt (Motorhersteller für DC-Motoren). Da es sich um eine Werbe-Email handelt, soll beim Öffnen möglichst gleich ersichtlich sein, ob das Produkt für den Empfänger brauchbar ist, sodass er in diesem Falle die 'nervige Werbe-Mail' nicht sofort löscht.
Aufgabenstellung
Bei dem 'Newsletter' soll es sich um eine einmalige Werbemail handeln, durch die potenzielle Kunden auf unser Produkt aufmerksam werden und mit uns in Kontakt treten, unsere Website besuchen oder sofort bestellen.
Das Produkt verfolgt einen eher ungewöhnlichen Ansatz, der den potenziellen Kunden eben ansprechen könnte oder nicht, da er damit selbst ein umfangreicheres Produkt anbieten könnte, sollte das in seinem Interesse sein.
Da dies ein neuer Ansatz für den potenziellen Kunden wäre, wird der Empfänger der Email nicht damit rechnen. Deshalb ist wichtig, dass beim Öffnen der Email sofort klar wird, was unser Produkt bietet und wie es unserem Kunden von Nutzen sein kann.
Es handelt sich bei den potenziellen Kunden um Motorhersteller (für DC-Motoren im Fahrzeug, bspw. Fensterheber), die diesen Motor selbst nicht ansteuern. Sie verkaufen diese Motoren also entweder ohne Steuerung oder kaufen die Steuerung von einem Dienstleister. Wir bieten eben diese Steuerung an, allerdings konfigurierbar auf die Anwendung des Kunden, sodass kein weiterer Entwicklungsaufwand entsteht. Der Kunde kann also entweder einen bestehenden Lieferanten für seine Steuerung durch uns ersetzen, da wir in der Lage sind, einen sehr niedrigen Stückpreis zu bieten, oder sein Geschäftsfeld erweitern.
Durch die Email soll sich der Empfänger um diesen Umstand und die Vorteile, die durch unser Produkt für ihn entstehen, bewusstwerden.
Beim Öffnen der Email soll der 'Eye-Catcher'-Bereich zu sehen sein, der den Kunden neugierig machen soll. Hat der Kunde Interesse, soll bei Scrollen mehr Information zu sehen sein.
Dieser 'Eye-Catcher'-Bereich ist in der anhängenden PowerPoint-Datei auf der ersten Seite enthalten. Beim Scrollen sollen die Informationen, die sich auf den nächsten Seiten befinden, zu sehen sein. Des Weiteren soll ein Foto der geöffneten ECU (anhängend) zu sehen sein, mit den Informationen zum Gehäuse, sowie zwei Screenshots der mitgelieferten GUI. Da ..

```html
<!DOCTYPE html>
<html lang="de">
<head>
<meta charset="utf-8">
<title>Veltrano Antriebstechnik – ECU für DC-Motoren</title>
<link href="https://fonts.googleapis.com/css2?family=Poppins:wght@400;500;600&family=Lato:wght@400;700&display=swap" rel="stylesheet">
<style>
  :root{
    --orange:#ff9c00;
    --orange-text:#f7941d;
    --blue:#0329c4;
    --white:#ffffff;
    --ink:#1d1d1d;
    --rule:#c9c9c9;
  }
  *{box-sizing:border-box;margin:0;padding:0}
  html,body{width:1200px;height:2247px;overflow:hidden}
  body{position:relative;background:var(--orange);font-family:"Lato",sans-serif;color:var(--ink)}
  .header{position:absolute;left:0;top:0;width:1200px;height:190px;background:var(--white);display:flex;align-items:center;justify-content:center}
  .brand{display:flex;align-items:center;gap:16px;font-family:"Poppins",sans-serif;font-weight:600;font-size:40px;color:var(--ink)}
  .brand-dot{width:26px;height:26px;border-radius:50%;background:var(--orange)}
  .card{position:absolute;background:var(--white);border-radius:10px}
  .card-side{top:256px;width:384px;height:661px;padding:36px 24px 0 24px}
  .card-left{left:24px}
  .card-right{left:792px}
  .card-title{font-family:"Poppins",sans-serif;font-weight:600;font-size:24px;line-height:32px;color:var(--orange-text);text-align:center;text-transform:uppercase}
  .card-rule{width:178px;height:1px;background:var(--rule);margin:22px auto 16px}
  .list{list-style:none;font-size:17.5px;line-height:34.5px;hyphens:auto;-webkit-hyphens:auto}
  .list>li{position:relative;padding-left:16px}
  .list>li::before{content:"";position:absolute;left:1px;top:13px;width:8px;height:8px;border-radius:50%;background:var(--orange-text)}
  .sublist{list-style:none}
  .sublist li{position:relative;padding-left:24px}
  .sublist li::before{content:"";position:absolute;left:2px;top:13px;width:8px;height:8px;border-radius:50%;border:1.5px solid var(--orange-text)}
  .card-center{left:408px;top:241px;width:384px;height:691px;background:var(--blue);border-radius:0;box-shadow:0 10px 28px rgba(0,0,40,.35);padding:38px 20px 0 24px;color:var(--white)}
  .card-center .card-title{color:var(--white);font-size:25px;line-height:33px}
  .card-center .card-rule{background:var(--white);width:178px;margin:20px auto 18px}
  .steps{list-style:none;font-size:17px;line-height:34.5px;font-weight:700;hyphens:auto;-webkit-hyphens:auto}
  .steps li{position:relative;padding-left:17px}
  .steps li::before{content:"";position:absolute;left:1px;top:13px;width:8px;height:8px;border-radius:50%;background:var(--white)}
  .steps strong{font-weight:700;text-shadow:0 0 .6px #fff}
  .panel{position:absolute;left:24px;width:1152px;background:var(--blue);border-radius:10px;color:var(--white);font-family:"Poppins",sans-serif;font-weight:500}
  .applications{top:961px;height:391px}
  .applications-text{position:absolute;left:60px;top:65px;width:590px;text-align:center;font-size:24px;line-height:42px}
  .ecu-photo{position:absolute;left:706px;top:35px;width:412px;height:322px;background:linear-gradient(135deg,#4a5a50 0%,#2b3a2f 45%,#8e9690 100%)}
  .features{top:1374px;height:210px;padding:40px 0 0 54px;display:grid;grid-template-columns:520px 520px;grid-auto-rows:37px;row-gap:8px;align-content:start}
  .feature{display:flex;align-items:center;gap:14px;font-size:24px;line-height:37px}
  .feature svg{flex:none}
  .details{left:24px;top:1606px;width:1152px;height:616px;padding:34px 40px 0 40px;font-family:"Poppins",sans-serif}
  .details-title{font-weight:500;font-size:27px;line-height:36px;color:var(--orange-text);margin-left:38px;margin-bottom:4px}
  .details .list{font-size:20.5px;line-height:36px;hyphens:manual}
  .details .list>li{padding-left:38px}
  .details .list>li::before{left:10px;top:14px}
  .details .gap{height:32px}
</style>
</head>
<body>
  <header class="header">
    <div class="brand"><span class="brand-dot"></span>Veltrano Antriebstechnik</div>
  </header>

  <section class="card card-side card-left">
    <h2 class="card-title">Technische<br>Vorteile</h2>
    <div class="card-rule"></div>
    <ul class="list">
      <li>Dank Halbleitertechnologie gegenüber Relais:
        <ul class="sublist">
          <li>Leiser</li>
          <li>Kein Verschleiß (Kontaktprellen, Lichtbogenentwicklung), kein Icing</li>
          <li>Sehr präzises Ansprechverhalten</li>
        </ul>
      </li>
      <li>Hohe Dynamik im Lastbereich: bis 19A (Stromspitzen bis 30A)</li>
      <li>Geringer Stromverbrauch:
        <ul class="sublist">
          <li>Sleep-Mode: &lt; 100 µA.</li>
          <li>On-Mode: &lt; 100 mA</li>
        </ul>
      </li>
      <li>Robust gegen Umwelteinflüsse</li>
    </ul>
  </section>

  <section class="card card-center">
    <h2 class="card-title">In wenigen Tagen<br>zur Fertigen</h2>
    <div class="card-rule"></div>
    <ul class="steps">
      <li>Ermitteln Sie Ihre Systemparameter mit unserem <strong>Komplettpaket</strong> zum An&shy;schluss an <strong>Ihren DC-Motor</strong></li>
      <li>Per einfachem Mausklick werden Ihre Parameter in unsere <strong>fertige Software</strong> geladen</li>
      <li>Sie können Ihre Einstellungen inner&shy;halb <strong>weniger Minuten testen</strong>, bis Sie mit unserer maßgeschneiderten Lösung zufrieden sind</li>
      <li>Wir erstellen das <strong>LIN</strong> File für Ihre Kom&shy;munikation mit dem System Ihres Kunden</li>
      <li>Die <strong>fertige ECU</strong> ist bereit für Ihre Bestellung</li>
    </ul>
  </section>

  <section class="card card-side card-right">
    <h2 class="card-title">Strategische<br>Vorteile</h2>
    <div class="card-rule"></div>
    <ul class="list">
      <li>Komplettpaket zur Ermittlung Ihrer Systemparameter (Strom-/ Span&shy;nungsschwellen, Timingparameter u.v.m.)</li>
      <li>ECU bewährt seit 2010</li>
      <li>HW-Stand 3. Generation</li>
      <li>Zertifiziert nach …</li>
      <li>Keine Basisentwicklung erforderlich</li>
      <li>Minimaler Aufwand bei Applikation durch GUI-Konfigurator</li>
      <li>Made in Germany</li>
      <li>Schneller geht’s nicht</li>
    </ul>
  </section>

  <section class="panel applications">
    <p class="applications-text">Fensterheber | elektrisch verstellbare Spiegel | Schiebedach | elektrische Sitzverstellung | Scheibenwischer&nbsp; Waschwasserpumpen | Türverriegelung | Spoilerverstellung | Beschattungssysteme |<br>elektrischer Heckklappenantrieb</p>
    <div class="ecu-photo" role="img" aria-label="Foto der geöffneten ECU mit grüner Platine im schwarzen Kunststoffgehäuse"></div>
  </section>

  <section class="panel features">
    <div class="feature"><svg width="20" height="16" viewBox="0 0 20 16"><path d="M2 8l5 5L18 2" fill="none" stroke="#fff" stroke-width="3.2" stroke-linecap="round" stroke-linejoin="round"/></svg>Anwendung</div>
    <div class="feature"><svg width="20" height="16" viewBox="0 0 20 16"><path d="M2 8l5 5L18 2" fill="none" stroke="#fff" stroke-width="3.2" stroke-linecap="round" stroke-linejoin="round"/></svg>bei hohem Lastbereich</div>
    <div class="feature"><svg width="20" height="16" viewBox="0 0 20 16"><path d="M2 8l5 5L18 2" fill="none" stroke="#fff" stroke-width="3.2" stroke-linecap="round" stroke-linejoin="round"/></svg>für DC Bürstenmotoren</div>
    <div class="feature"><svg width="20" height="16" viewBox="0 0 20 16"><path d="M2 8l5 5L18 2" fill="none" stroke="#fff" stroke-width="3.2" stroke-linecap="round" stroke-linejoin="round"/></svg>mit schnellen Schaltzeiten</div>
    <div class="feature"><svg width="20" height="16" viewBox="0 0 20 16"><path d="M2 8l5 5L18 2" fill="none" stroke="#fff" stroke-width="3.2" stroke-linecap="round" stroke-linejoin="round"/></svg>in einer LIN-Umgebung</div>
    <div class="feature"><svg width="20" height="16" viewBox="0 0 20 16"><path d="M2 8l5 5L18 2" fill="none" stroke="#fff" stroke-width="3.2" stroke-linecap="round" stroke-linejoin="round"/></svg>präzisen Positionsinformationen.</div>
  </section>

  <section class="card details">
    <h3 class="details-title">Mit unserer ECU sparen Sie Kosten, da</h3>
    <ul class="list">
      <li>wir aufgrund eines langjährigen Skaleneffekts einen niedrigen Stückpreis anbieten</li>
      <li>Keine Entwicklungskosten entstehen</li>
      <li>für Sie kaum Aufwand bei der Konfiguration entsteht – unser Entwicklungstool mit Realtime Strom- und Spannungsmessung erleichtert die schnelle Applikation</li>
      <li>Sie von uns ein kostenloses Konfigurationspaket zur Verfügung gestellt bekommen – es fallen für Sie bis zur Bestellung keine Kosten an!</li>
    </ul>
    <div class="gap"></div>
    <h3 class="details-title">Gehäuse</h3>
    <ul class="list">
      <li>12-poliger KTX-Stecker</li>
      <li>2-Komponenten Vergusstechnologie auf Silikonbasis</li>
      <li>IP53</li>
      <li>Material: PA6-GF15</li>
      <li>Einfaches Clip-System zur Befestigung</li>
      <li>Alternatives Gehäuse auf Anfrage</li>
    </ul>
  </section>
</body>
</html>
```